Orbeo app design for cryptocurrency trading investment fund Vornexa

Vornexa is an investment fund that help investors with investing in cryptocurrencies such as Zentrix and Pallidor. We use our own trading platform to buy and sell crypto currencies on behalf of the investors. As an extra service we want to develop an Orbeo app for our investors. After logging in the Orbeo app they can get a real-time insight in the value of their portfolio. We have created wireframes of these pages in attached zip file. This zip file also contains the logo of Vornexa.

We need you to design a clean professional and fresh app design based on the wireframes. The app design should contain the corporate identity of Vornexa and thus the following color codes and font type must be used:

Color 1: 489e95
Color 2: 474646
Font type: Open Sans

login.png
The investor first has to login the app

home.png
The first page the investor sees after logging in.

account.png
In the account section the investor can change his login access details to the app

account_b.png
On this page he can change his password.

Coin page (added as separate file)
This is the page that shows up when you click on one of the coins.

Target Market(s)

Investors who invest the minimum amount of € 100.000

Industry/Entity Type

Tech

Requirements
Must have
• Professional modern design
Should not have
• cheap colourful creative look and feel.

```html
<!DOCTYPE html>
<html lang="en">
<head>
<meta charset="utf-8">
<title>Vornexa – Orbeo app screens</title>
<link href="https://fonts.googleapis.com/css2?family=Open+Sans:ital,wght@0,300;0,400;0,600;0,700;1,400&display=swap" rel="stylesheet">
<style>
:root{
  --teal:#489e95;
  --charcoal:#474646;
  --bar:#2e2e2e;
  --bg:#d6d6d6;
  --white:#ffffff;
  --panel:#f1f1f1;
  --line:#e2e2e2;
  --muted:#8d8d8d;
  --text:#3b3b3b;
  --red:#d9343d;
  --btn:#ececec;
  --orange:#f39a1e;
}
*{box-sizing:border-box;margin:0;padding:0}
html,body{width:1200px;height:819px;overflow:hidden}
body{background:var(--bg);font-family:"Open Sans",Arial,sans-serif;color:var(--text)}
.stage{width:1200px;height:819px;display:flex;justify-content:center;align-items:center;gap:60px}
.screen{width:330px;height:587px;background:var(--white);position:relative;overflow:hidden;box-shadow:0 6px 24px rgba(0,0,0,.18)}
.status{height:21px;background:var(--bar);color:#fff;font-size:9px;display:flex;align-items:center;justify-content:space-between;padding:0 8px}
.status .dots{letter-spacing:-1px}
.status .batt{display:flex;align-items:center;gap:4px}
.status .batt i{display:inline-block;width:18px;height:8px;border:1px solid #fff;background:#fff;border-radius:1px}
.appbar{height:47px;background:var(--charcoal);color:#fff;display:flex;align-items:center;justify-content:space-between;padding:0 12px}
.appbar h1{font-size:12px;font-weight:700;letter-spacing:.5px}
.bell{position:relative;width:26px;height:22px}
.bell b{position:absolute;right:-2px;top:-3px;background:var(--teal);color:#fff;font-size:8px;font-weight:700;width:12px;height:12px;border-radius:2px;display:flex;align-items:center;justify-content:center}

/* login */
.brand{position:absolute;top:118px;left:0;right:0;text-align:center}
.brand .name{display:inline-flex;align-items:center;gap:8px;font-size:44px;font-weight:400;color:var(--charcoal);line-height:1}
.brand .name span.mark{width:30px;height:30px;border-radius:50%;background:var(--teal)}
.brand p{font-size:13px;font-weight:300;color:#555;margin-top:8px}
.field{position:absolute;left:29px;right:29px;border-bottom:1.5px solid var(--charcoal);height:22px;display:flex;align-items:center;gap:6px;font-size:11px;text-transform:uppercase;color:#333}
.field svg{flex:none}
.keep{position:absolute;right:29px;top:350px;display:flex;align-items:center;gap:6px;font-size:11px;color:#333}
.keep .box{width:14px;height:14px;border:1.5px solid var(--teal)}
.pill{position:absolute;left:29px;right:29px;height:45px;border-radius:23px;background:var(--btn);font-size:12px;font-weight:700;letter-spacing:.5px;display:flex;align-items:center;justify-content:center;color:#333}
.forgot{position:absolute;bottom:18px;left:0;right:0;text-align:center;font-size:11px;font-style:italic;color:#9a9a9a}

/* home */
.summary{padding:0 12px;background:#fff;position:relative;z-index:1;box-shadow:0 2px 4px rgba(0,0,0,.12)}
.summary .row{display:flex;align-items:center;height:37px;border-bottom:1px solid var(--line);font-size:11px}
.summary .row:last-child{border-bottom:none}
.summary .lbl{flex:1}
.summary .amt{width:110px;text-align:right;font-size:14px;font-weight:300;color:var(--muted)}
.summary .pct{width:58px;text-align:right;font-size:14px;font-weight:300;color:var(--muted)}
.summary .up::after{content:"";display:inline-block;border:4px solid transparent;border-bottom:6px solid var(--teal);border-top:0;margin-left:5px;vertical-align:2px}
.summary .total .lbl{font-weight:700}
.summary .total .amt,.summary .total .pct{font-weight:700;color:#222}
.coins{background:var(--panel);padding:10px 12px 4px}
.coins table{width:100%;border-collapse:collapse;font-size:10.5px;text-align:center}
.coins td,.coins th{height:27px;border-right:1px solid var(--line);border-bottom:1px solid var(--line)}
.coins tr>*:last-child{border-right:none}
.coins tr:last-child td{border-bottom:none}
.coins .key{text-align:right;padding-right:5px;font-size:9px;color:var(--muted);width:50px}
.coins th{font-weight:700;font-size:10.5px;height:44px;vertical-align:bottom;padding-bottom:4px}
.coins th .dot{display:block;width:14px;height:14px;border-radius:50%;background:#555;margin:0 auto 4px}
.coins .pos{color:var(--teal)}
.coins .neg{color:var(--red)}
.chart{background:var(--panel);padding:8px 12px 12px}
.chart h2{font-size:11px;font-weight:400;color:#333;margin-bottom:3px}
.tabs{display:flex;align-items:center;gap:0}
.seg{display:flex;border:1px solid #ddd;border-radius:4px;background:#f6f6f6;overflow:hidden;height:22px}
.seg span{width:37.5px;display:flex;align-items:center;justify-content:center;font-size:9.5px;color:#aaa;border-right:1px solid #ddd}
.seg span:last-child{border-right:none}
.seg .on{background:#fff;color:#222;font-weight:600}
.dl{margin-left:auto;width:24px;height:24px;border-radius:50%;background:var(--teal);display:flex;align-items:center;justify-content:center}
.plot{background:#fff;margin-top:5px;height:137px}

/* account */
.avatar{position:absolute;top:142px;left:50%;margin-left:-23px;width:46px;height:46px;border-radius:50%;border:1.5px solid var(--charcoal);display:flex;align-items:center;justify-content:center}
.email{position:absolute;top:196px;left:0;right:0;text-align:center;font-size:13.5px;font-weight:700;color:#333}
.section{position:absolute;top:326px;left:0;right:0;text-align:center;font-size:12.5px;font-weight:300;color:#555}
.divider{position:absolute;top:347px;left:0;right:0;height:12px}
</style>
</head>
<body>
<main class="stage">

  <!-- Login -->
  <section class="screen login">
    <div class="status"><span class="dots">●●●●● Carrier</span><span>5:30PM</span><span class="batt">100% <i></i></span></div>
    <div class="brand">
      <div class="name"><span class="mark"></span>Vornexa</div>
      <p>Welcome to the Vornexa App</p>
    </div>
    <div class="field" style="top:259px">
      <svg width="14" height="10" viewBox="0 0 14 10"><rect width="14" height="10" fill="#333"/><path d="M0 0 L7 6 L14 0" stroke="#fff" stroke-width="1.2" fill="none"/></svg>Email
    </div>
    <div class="field" style="top:306px">
      <svg width="12" height="14" viewBox="0 0 12 14"><path d="M3 6V4a3 3 0 0 1 6 0v2" stroke="#333" stroke-width="1.8" fill="none"/><rect y="6" width="12" height="8" rx="1" fill="#333"/></svg>Password
    </div>
    <div class="keep">
      <span class="box"><svg width="11" height="11" viewBox="0 0 11 11"><path d="M1.5 5.5 L4.5 8.5 L10 1.5" stroke="#489e95" stroke-width="1.8" fill="none"/></svg></span>Stay logged in
    </div>
    <div class="pill" style="top:385px">LOGIN</div>
    <div class="forgot">Forgot password?</div>
  </section>

  <!-- Home -->
  <section class="screen home">
    <div class="status"><span class="dots">●●●●● Carrier</span><span>5:30PM</span><span class="batt">100% <i></i></span></div>
    <header class="appbar">
      <svg width="18" height="14" viewBox="0 0 18 14"><path d="M0 1h18M0 7h18M0 13h18" stroke="#fff" stroke-width="2"/></svg>
      <h1>VORNEXA</h1>
      <div class="bell"><svg width="20" height="20" viewBox="0 0 20 20"><path d="M10 2c-3 0-5 2.5-5 5.5V12l-2 3h14l-2-3V7.5C15 4.5 13 2 10 2z" fill="#fff"/><circle cx="10" cy="17" r="2" fill="#fff"/></svg><b>3</b></div>
    </header>
    <div class="summary">
      <div class="row"><span class="lbl">Invested Amount:</span><span class="amt">€100,000.00</span><span class="pct">100%</span></div>
      <div class="row"><span class="lbl">Current Balance:</span><span class="amt">€110,000.00</span><span class="pct up">110%</span></div>
      <div class="row total"><span class="lbl">Profit/Loss:</span><span class="amt">€ 10,000.00</span><span class="pct up">10%</span></div>
    </div>
    <div class="coins">
      <table>
        <tr><th class="key" style="font-weight:400">COINS</th><th><i class="dot"></i>PAL/EUR</th><th><i class="dot" style="background:#5a7fa8"></i>KVR</th><th><i class="dot" style="background:#4a8bbf"></i>NLO</th><th><i class="dot" style="background:var(--orange)"></i>ZTX</th><th><i class="dot" style="background:#2fa86d"></i>QRA</th></tr>
        <tr><td class="key">CHANGE</td><td class="pos">+9.4%</td><td class="neg">-15.11%</td><td class="pos">+4.4%</td><td class="pos">+1.6%</td><td class="pos">+9.24%</td></tr>
        <tr><td class="key">PRICE (€)</td><td>295.22</td><td>45.89</td><td>235.56</td><td>2,400.05</td><td>2.03</td></tr>
        <tr><td class="key">HOLDINGS</td><td>2.552</td><td>132.009</td><td>38.236</td><td>59.60</td><td>4.952</td></tr>
        <tr><td class="key">H (€)</td><td>755.87K</td><td>556.72K</td><td>255.40K</td><td>143.36K</td><td>10.044</td></tr>
      </table>
    </div>
    <div class="chart">
      <h2>PORTFOLIO CHART</h2>
      <div class="tabs">
        <div class="seg"><span>1D</span><span>7D</span><span>1M</span><span class="on">3M</span><span>6M</span><span>1Y</span><span>ALL</span></div>
        <div class="dl"><svg width="12" height="12" viewBox="0 0 12 12"><path d="M6 1v7M3 5l3 3 3-3M2 11h8" stroke="#fff" stroke-width="1.8" fill="none"/></svg></div>
      </div>
      <svg class="plot" width="306" height="137" viewBox="0 0 306 137">
        <g font-family="Open Sans, sans-serif" font-size="7" fill="#666">
          <text x="4" y="14">400</text><text x="4" y="42">300</text><text x="4" y="70">200</text><text x="4" y="98">100</text>
          <text x="96" y="132">APRIL</text><text x="192" y="132">MAY</text><text x="286" y="132">JUNE</text>
        </g>
        <g stroke="#e4e4e4" stroke-width="1">
          <path d="M24 11H300M24 39H300M24 67H300M24 95H300M24 122H300"/>
          <path d="M24 8V122M114 8V122M207 8V122M296 8V122"/>
        </g>
        <polyline fill="none" stroke="#489e95" stroke-width="2" points="24,99 45,105 70,100 92,106 116,75 134,82 158,74 182,72 205,51 229,71 252,12 275,54 298,35"/>
      </svg>
    </div>
  </section>

  <!-- Account -->
  <section class="screen account">
    <div class="status"><span class="dots">●●●●● Carrier</span><span>5:30PM</span><span class="batt">100% <i></i></span></div>
    <header class="appbar">
      <svg width="18" height="14" viewBox="0 0 18 14"><path d="M0 1h18M0 7h18M0 13h18" stroke="#fff" stroke-width="2"/></svg>
      <h1>ACCOUNT</h1>
      <div class="bell"><svg width="20" height="20" viewBox="0 0 20 20"><path d="M10 2c-3 0-5 2.5-5 5.5V12l-2 3h14l-2-3V7.5C15 4.5 13 2 10 2z" fill="#fff"/><circle cx="10" cy="17" r="2" fill="#fff"/></svg><b>3</b></div>
    </header>
    <div class="avatar"><svg width="16" height="11" viewBox="0 0 16 11"><rect width="16" height="11" fill="#333"/><path d="M0 0 L8 6.5 L16 0" stroke="#fff" stroke-width="1.2" fill="none"/></svg></div>
    <div class="email">marten@vornexa.com</div>
    <div class="section">Change Password</div>
    <svg class="divider" width="330" height="12" viewBox="0 0 330 12"><path d="M0 1H153L165 11L177 1H330" stroke="#e0e0e0" stroke-width="1.5" fill="none"/></svg>
    <div class="field" style="top:393px">
      <svg width="12" height="14" viewBox="0 0 12 14"><path d="M3 6V4a3 3 0 0 1 6 0v2" stroke="#333" stroke-width="1.8" fill="none"/><rect y="6" width="12" height="8" rx="1" fill="#333"/></svg>Old password
    </div>
    <div class="field" style="top:440px">
      <svg width="12" height="14" viewBox="0 0 12 14"><path d="M3 6V4a3 3 0 0 1 6 0v2" stroke="#333" stroke-width="1.8" fill="none"/><rect y="6" width="12" height="8" rx="1" fill="#333"/></svg>New password
    </div>
    <div class="pill" style="top:518px">CHANGE</div>
  </section>

</main>
</body>
</html>
```